Recruitment website for new startup company - Calder Ashby Recruitment

Hi , I need to design a web page for my new recruitment company with the ability to link to social media accounts. The ability to add and remove job posts along with a blog page which I can update. More importantly I need the website to have the functionality of applicants being able to upload their cv and somewhere for me to store it. I will need assistance/recommendation for email address with company name, hosting and security. An about us page. The website will also need a search function for applicants to narrow down the search. Again I will need to be able to update this myself as the company grows. I have my logo ready domain address ready and would like the web site done ASAP. Thank you for your help.
Updates

Reason: Want to get a few more ideas and variations to designs done. But using logo as inspiration Thanks

Target Market(s)

Financial and property industry so professionals. New starters to senior management age range 25-60

Industry/Entity Type

Financial

Coding

Coded - Design and coding required

Number of Pages Required

4 page

Colors

Designer to choose colors to be used in the design.

Requirements
Must have
• Ability for me to add amend and remove job posts, ability for applicants to upload cv and for me to store and access it. Link to social media accounts
Should not have
• Needs to be clean approachable so not to childish but must come across as approachable and trustworthy.
• No yellow please my logo has a gold V not yellow. If it looks yellow use a different colour please. Thanks

```html
<!DOCTYPE html>
<html lang="en">
<head>
<meta charset="utf-8">
<title>Calder Ashby Recruitment</title>
<link rel="stylesheet" href="https://fonts.googleapis.com/css2?family=Outfit:wght@300;400;500;600;700&display=swap">
<style>
:root{
  --navy:#1d3461;
  --hero:#284a7e;
  --gold:#c3a066;
  --gold-text:#d2b27c;
  --text:#1d3461;
  --muted:#777d88;
  --green:#5fbf4f;
  --rule:#e3e5ea;
  --faint:#eef0f4;
  --white:#ffffff;
}
*{box-sizing:border-box;margin:0;padding:0}
html,body{width:1174px;height:1200px;overflow:hidden;background:var(--white)}
body{font-family:"Outfit",sans-serif;color:var(--text);position:relative}
.page{position:relative;width:1174px;height:1200px;overflow:hidden}

/* hero */
.hero{position:absolute;left:0;top:0;width:1174px;height:336px}
.hero-bg{position:absolute;inset:0}
.brand{position:absolute;left:82px;top:62px;color:var(--white);font-weight:400;letter-spacing:2px;line-height:1.15}
.brand-name{display:block;font-size:23px}
.brand-sub{display:block;font-size:13px;letter-spacing:3.4px}
.account{position:absolute;right:70px;top:41px;font-size:10px;color:var(--white);font-weight:300}
.account span{margin:0 6px}
.nav{position:absolute;right:70px;top:73px;display:flex;gap:30px}
.nav a{color:var(--white);text-decoration:none;font-size:15px;font-weight:600}
.hero-title{position:absolute;left:0;width:100%;top:140px;text-align:center;color:var(--gold-text);font-size:25px;font-weight:600}
.hero-lead{position:absolute;left:0;width:100%;top:175px;text-align:center;color:#e4e9f2;font-size:13px;font-weight:300}
.search{position:absolute;left:263px;top:210px;display:flex;gap:14px}
.search-fields{display:flex;background:var(--white);border-radius:4px;height:41px;box-shadow:0 2px 4px rgba(0,0,0,.15)}
.field{display:flex;align-items:center;padding-left:16px;font-size:11.5px;color:#555c68;border-right:1px solid #cfd3da}
.field:last-child{border-right:none}
.field.keywords{width:196px}.field.location{width:196px}.field.sector{width:127px}
.field svg{margin-left:2px}
.btn-gold{background:var(--gold);color:var(--navy);font-size:11.5px;font-weight:600;border-radius:4px;display:flex;align-items:center;justify-content:center;box-shadow:0 2px 4px rgba(0,0,0,.15)}
.search .btn-gold{width:127px;height:41px}

/* steps */
.intro{position:absolute;left:0;top:404px;width:100%;text-align:center}
.intro h2{font-size:25px;font-weight:600;color:var(--navy)}
.intro h2 em{font-style:normal;color:var(--gold);border-bottom:2px solid var(--gold)}
.intro p{margin-top:8px;font-size:13px;color:var(--muted);font-weight:300}
.steps{position:absolute;top:500px;left:0;width:100%;height:90px}
.step{position:absolute;width:120px;margin-left:-60px;text-align:center}
.step svg{display:block;margin:0 auto}
.step span{display:block;margin-top:6px;font-size:13px;font-weight:600;color:var(--navy)}

/* listings */
.section-head{position:absolute;top:650px;font-size:16.5px;font-weight:500;color:var(--navy);border-bottom:2px solid var(--rule);height:36px}
.recent-head{left:82px;width:737px}
.featured-head{left:850px;width:255px}
.pager{position:absolute;top:659px;left:765px;display:flex;gap:13px}
.pager i{width:20px;height:20px;background:var(--navy);border-radius:2px;display:flex;align-items:center;justify-content:center}
.job-list{position:absolute;left:83px;top:706px;width:736px;border:1px solid var(--rule)}
.job{position:relative;border-bottom:1px solid var(--rule)}
.job:last-child{border-bottom:none}
.job h3{position:absolute;left:27px;top:20px;font-size:15px;font-weight:600;color:var(--navy)}
.job .place{position:absolute;left:19px;top:44px;font-size:13px;color:#3c4a66;font-weight:300;display:flex;align-items:center;gap:3px}
.job .timer{position:absolute;left:19px;top:66px;font-size:11px;font-weight:600;color:#3c4a66;display:flex;align-items:center;gap:3px}
.job .pay{position:absolute;left:316px;top:22px;font-size:12px;color:var(--muted);font-weight:300}
.job .type{position:absolute;left:316px;top:46px;font-size:11px;color:var(--green);font-weight:300}
.btn-outline{border:2px solid var(--navy);border-radius:5px;width:126px;height:40px;display:flex;align-items:center;justify-content:center;font-size:11.5px;font-weight:600;color:var(--navy);background:var(--white)}
.job .btn-outline{position:absolute;left:588px;top:29px}
.job.short .btn-outline{top:20px}
.more-jobs{position:absolute;left:670px;top:1097px;width:128px;height:40px}

.featured{position:absolute;left:858px;top:706px;width:234px;height:338px;border:1px solid var(--rule)}
.featured-photo{height:96px;background:linear-gradient(120deg,#2a1a16 0%,#4a2b1e 45%,#7a2f1c 70%,#2d1c18 100%)}
.featured-body{padding:18px 16px 0}
.featured h3{font-size:15px;font-weight:600;color:var(--navy)}
.featured .place{margin-top:7px;font-size:13px;color:#3c4a66;font-weight:300}
.featured .pay{margin-top:6px;font-size:12px;color:var(--muted);font-weight:300}
.featured .type{margin-top:5px;font-size:11px;color:var(--green);font-weight:300}
.featured .summary{margin-top:20px;font-size:11.5px;line-height:21px;color:#3c4a66;font-weight:300}
.featured-more{position:absolute;left:966px;top:1060px}
.footer-rule{position:absolute;left:0;bottom:0;width:100%;height:3px;background:var(--navy)}
</style>
</head>
<body>
<div class="page">
  <header class="hero">
    <svg class="hero-bg" width="1174" height="336" viewBox="0 0 1174 336" role="img" aria-label="Office workspace photograph behind a navy overlay">
      <defs>
        <linearGradient id="heroFill" x1="0" y1="0" x2="1" y2="1">
          <stop offset="0" stop-color="#2b4d82"/>
          <stop offset="0.6" stop-color="#284a7e"/>
          <stop offset="1" stop-color="#2f5287"/>
        </linearGradient>
      </defs>
      <path d="M0 0H1174V260Q587 410 0 260Z" fill="url(#heroFill)"/>
    </svg>
    <div class="brand"><span class="brand-name">CALDER ASHBY</span><span class="brand-sub">RECRUITMENT</span></div>
    <div class="account">Log In<span>|</span>Register</div>
    <nav class="nav"><a href="#">Home.</a><a href="#">About.</a><a href="#">Recruitment.</a><a href="#">News.</a><a href="#">Contact.</a></nav>
    <h1 class="hero-title">Multi-Industry Recruitment Agency</h1>
    <p class="hero-lead">Select your sector and/or type job keywords, then click search to find your perfect job.</p>
    <form class="search">
      <div class="search-fields">
        <div class="field keywords">Job Keywords</div>
        <div class="field location">Location<svg width="9" height="6" viewBox="0 0 9 6"><path d="M1 1l3.5 3.5L8 1" fill="none" stroke="#555c68" stroke-width="1"/></svg></div>
        <div class="field sector">Sector<svg width="9" height="6" viewBox="0 0 9 6"><path d="M1 1l3.5 3.5L8 1" fill="none" stroke="#555c68" stroke-width="1"/></svg></div>
      </div>
      <div class="btn-gold">Search</div>
    </form>
  </header>

  <section class="intro">
    <h2>All the jobs you want in <em>one</em> simple place.</h2>
    <p>Find the jobs you want in just a few simple clicks.</p>
  </section>

  <section class="steps">
    <div class="step" style="left:410px">
      <svg width="60" height="56" viewBox="0 0 60 56">
        <text x="10" y="50" font-family="Outfit,sans-serif" font-size="54" font-weight="700" fill="#eef0f4">1</text>
        <circle cx="31" cy="22" r="11" fill="none" stroke="#1d3461" stroke-width="2.4"/>
        <path d="M23 30l-6 9" stroke="#1d3461" stroke-width="2.4" stroke-linecap="round"/>
        <path d="M14 48h24" stroke="#1d3461" stroke-width="2.4"/><circle cx="42" cy="48" r="1.3" fill="#1d3461"/>
      </svg>
      <span>SEARCH</span>
    </div>
    <div class="step" style="left:586px">
      <svg width="60" height="56" viewBox="0 0 60 56">
        <text x="14" y="50" font-family="Outfit,sans-serif" font-size="54" font-weight="700" fill="#eef0f4">2</text>
        <path d="M21 40l3-9 17-17 6 6-17 17z" fill="none" stroke="#1d3461" stroke-width="2.2" stroke-linejoin="round"/>
        <path d="M37 18l6 6" stroke="#1d3461" stroke-width="2"/>
        <path d="M16 48h30" stroke="#1d3461" stroke-width="2.4"/>
      </svg>
      <span>APPLY</span>
    </div>
    <div class="step" style="left:770px">
      <svg width="60" height="64" viewBox="0 0 60 64" style="margin-top:-8px">
        <text x="14" y="58" font-family="Outfit,sans-serif" font-size="54" font-weight="700" fill="#eef0f4">3</text>
        <path d="M30 46c-5-7-10-13-10-19a10 10 0 0 1 20 0c0 6-5 12-10 19z" fill="none" stroke="#1d3461" stroke-width="2.2"/>
        <path d="M18 56h24" stroke="#1d3461" stroke-width="2.4"/>
        <path d="M29 4l-2 6M38 6l-3 5M22 12l4 2M42 13l-4 2" stroke="#1d3461" stroke-width="1.3"/>
        <circle cx="20" cy="5" r="1.2" fill="none" stroke="#1d3461"/><circle cx="17" cy="16" r="1.2" fill="none" stroke="#1d3461"/><circle cx="34" cy="14" r="1" fill="#1d3461"/>
      </svg>
      <span>HIRED</span>
    </div>
  </section>

  <h2 class="section-head recent-head">Recent Jobs</h2>
  <div class="pager">
    <i><svg width="6" height="9" viewBox="0 0 6 9"><path d="M5 1L1.5 4.5 5 8" fill="none" stroke="#fff" stroke-width="1.2"/></svg></i>
    <i><svg width="6" height="9" viewBox="0 0 6 9"><path d="M1 1l3.5 3.5L1 8" fill="none" stroke="#fff" stroke-width="1.2"/></svg></i>
  </div>
  <h2 class="section-head featured-head">Featured Job</h2>

  <div class="job-list">
    <article class="job" style="height:100px">
      <h3>Sales &amp; Marketing Coordinator</h3>
      <p class="place"><svg width="5" height="7" viewBox="0 0 5 7"><path d="M2.5 7C1 5 0 3.7 0 2.5a2.5 2.5 0 0 1 5 0C5 3.7 4 5 2.5 7z" fill="#8a93a3"/></svg>Germany, Hanover</p>
      <p class="timer"><svg width="6" height="6" viewBox="0 0 6 6"><circle cx="3" cy="3" r="2.4" fill="none" stroke="#8a93a3"/></svg>65 days 21:46:59</p>
      <p class="pay">£27500</p><p class="type">Full Time</p>
      <div class="btn-outline">View More</div>
    </article>
    <article class="job" style="height:100px">
      <h3>ENGINEERING TECHNICIAN</h3>
      <p class="place"><svg width="5" height="7" viewBox="0 0 5 7"><path d="M2.5 7C1 5 0 3.7 0 2.5a2.5 2.5 0 0 1 5 0C5 3.7 4 5 2.5 7z" fill="#8a93a3"/></svg>Netherlands, Rotterdam</p>
      <p class="timer"><svg width="6" height="6" viewBox="0 0 6 6"><circle cx="3" cy="3" r="2.4" fill="none" stroke="#8a93a3"/></svg>42 days 20:41:55</p>
      <p class="pay">£27500 - £30000</p><p class="type">Full Time</p>
      <div class="btn-outline">View More</div>
    </article>
    <article class="job short" style="height:80px">
      <h3>SCIENCE TEACHER</h3>
      <p class="place"><svg width="5" height="7" viewBox="0 0 5 7"><path d="M2.5 7C1 5 0 3.7 0 2.5a2.5 2.5 0 0 1 5 0C5 3.7 4 5 2.5 7z" fill="#8a93a3"/></svg>England, London, Camden</p>
      <p class="pay">£30000 - £32500</p><p class="type">Full Time</p>
      <div class="btn-outline">View More</div>
    </article>
    <article class="job short" style="height:80px">
      <h3 style="top:18px">ACCOUNTS ASSISTANT</h3>
      <p class="place" style="top:42px"><svg width="5" height="7" viewBox="0 0 5 7"><path d="M2.5 7C1 5 0 3.7 0 2.5a2.5 2.5 0 0 1 5 0C5 3.7 4 5 2.5 7z" fill="#8a93a3"/></svg>England, Hampsire, Gosport</p>
      <p class="pay" style="top:20px">£31900 - £36970</p><p class="type" style="top:44px">Full Time</p>
      <div class="btn-outline">View More</div>
    </article>
  </div>
  <div class="btn-gold more-jobs">View More</div>

  <article class="featured">
    <div class="featured-photo" role="img" aria-label="Photograph of a neon restaurant sign"></div>
    <div class="featured-body">
      <h3>STEAK HOUSE MANAGER</h3>
      <p class="place">Netherlands, Rotterdam</p>
      <p class="pay">£27500 - £30000</p>
      <p class="type">Full Time</p>
      <p class="summary">Lorem ipsum dolor sit amet, consectetur adipiscing elit. In tristique elit eget purus malesuada, vitae imperdiet tortor viverra In tristique elit eget purus...</p>
    </div>
  </article>
  <div class="btn-outline featured-more">View More</div>

  <div class="footer-rule"></div>
</div>
</body>
</html>
```